Brimvaxo.com protective pads need Ads to sell products

We manufacture protective pads for car doors and are looking for ads to bring customers to the site on Facebook, twitter and display advertising. We need ads that get the message over that damage caused when parked is expensive and frequent and our pads will protect your car from this type of damage. This is a new product that we are starting to sell

```html
<!DOCTYPE html>
<html lang="en">
<head>
<meta charset="utf-8">
<title>Brimvaxo door pads – ad set</title>
<link rel="stylesheet" href="https://fonts.googleapis.com/css2?family=Bebas+Neue&family=Montserrat:wght@400;500;700;800&display=swap">
<style>
  :root{
    --sheet:#dadada;
    --ink:#111111;
    --red:#d4171d;
    --red-deep:#8e0d11;
    --panel-a:#262626;
    --panel-b:#0b0b0b;
    --white:#ffffff;
    --muted:#d9d9d9;
  }
  *{margin:0;padding:0;box-sizing:border-box}
  html,body{width:1200px;height:1200px;overflow:hidden;background:var(--sheet)}
  body{position:relative;font-family:"Montserrat",sans-serif;color:var(--white)}

  .ad{position:absolute;overflow:hidden;
      background:radial-gradient(ellipse at 70% 40%,var(--panel-a) 0%,var(--panel-b) 75%)}
  .ad > *{position:absolute}
  .ad__corner{left:0;top:0}
  .ad__corner polygon{fill:var(--red)}
  .ad__photo{border-radius:6px;
      background:radial-gradient(ellipse at 55% 65%,#c3232a 0%,#7a1418 38%,rgba(40,40,40,.6) 70%,rgba(20,20,20,0) 100%)}
  .ad__prevents{font-weight:800;line-height:1;letter-spacing:.02em;white-space:nowrap}
  .ad__headline{font-family:"Bebas Neue",sans-serif;color:var(--red);line-height:1;white-space:nowrap;letter-spacing:-.01em}
  .ad__sub{font-weight:400;line-height:1;letter-spacing:.04em;white-space:nowrap}
  .ad__url{font-weight:500;color:var(--muted);line-height:1;white-space:nowrap}
  .ad__brand{display:flex;align-items:center;font-weight:700;line-height:1;white-space:nowrap}
  .ad__brand::before{content:"";display:block;width:.8em;height:.8em;background:var(--red);margin-right:.35em}
  .ad__cta{display:flex;align-items:center;justify-content:center;gap:.3em;background:var(--red);
      border:1px solid var(--white);border-radius:999px;font-weight:500;line-height:1;white-space:nowrap}
  .ad__cta svg{width:1em;height:1em}

  .label{position:absolute;transform:translateX(-50%);font-weight:800;color:var(--ink);line-height:1;letter-spacing:.02em;white-space:nowrap}

  /* Facebook 620 x 325 */
  .ad--facebook{left:74px;top:115px;width:620px;height:325px}
  .ad--facebook .ad__photo{left:22px;top:17px;width:304px;height:270px}
  .ad--facebook .ad__brand{right:24px;top:52px;font-size:16px}
  .ad--facebook .ad__prevents{right:16px;top:107px;font-size:27px}
  .ad--facebook .ad__headline{right:18px;top:138px;font-size:56px}
  .ad--facebook .ad__sub{right:22px;top:196px;font-size:27px}
  .ad--facebook .ad__cta{right:27px;top:254px;width:134px;height:25px;font-size:15px}
  .ad--facebook .ad__url{left:43px;top:292px;font-size:10px;letter-spacing:4px}

  /* Twitter 622 x 350 */
  .ad--twitter{left:74px;top:510px;width:622px;height:350px}
  .ad--twitter .ad__photo{left:22px;top:36px;width:288px;height:270px}
  .ad--twitter .ad__brand{right:24px;top:60px;font-size:18px}
  .ad--twitter .ad__prevents{right:16px;top:117px;font-size:30px}
  .ad--twitter .ad__headline{right:18px;top:146px;font-size:62px}
  .ad--twitter .ad__sub{right:18px;top:210px;font-size:29px}
  .ad--twitter .ad__cta{right:20px;top:269px;width:172px;height:31px;font-size:20px}
  .ad--twitter .ad__url{left:58px;top:318px;font-size:13px;letter-spacing:5px}

  /* Leaderboard 665 x 86 */
  .ad--leaderboard{left:76px;top:936px;width:665px;height:86px}
  .ad--leaderboard .ad__photo{left:52px;top:2px;width:112px;height:82px}
  .ad--leaderboard .ad__prevents{left:180px;top:11px;font-size:14px}
  .ad--leaderboard .ad__headline{left:180px;top:24px;font-size:46px}
  .ad--leaderboard .ad__sub{left:180px;top:65px;font-size:14px;letter-spacing:.02em}
  .ad--leaderboard .ad__cta{left:436px;top:34px;width:104px;height:22px;font-size:12px}
  .ad--leaderboard .ad__brand{right:18px;top:40px;font-size:12px}
  .ad--leaderboard .ad__url{right:13px;top:67px;font-size:6px;letter-spacing:1.5px}

  /* Banner 462 x 58 */
  .ad--banner{left:82px;top:1070px;width:462px;height:58px}
  .ad--banner .ad__photo{left:34px;top:2px;width:80px;height:52px}
  .ad--banner .ad__prevents{left:125px;top:6px;font-size:9.5px}
  .ad--banner .ad__headline{left:125px;top:15px;font-size:32px}
  .ad--banner .ad__sub{left:125px;top:44px;font-size:9px;letter-spacing:.02em}
  .ad--banner .ad__cta{left:306px;top:23px;width:61px;height:13px;font-size:7px}
  .ad--banner .ad__brand{right:16px;top:22px;font-size:8px}
  .ad--banner .ad__url{right:11px;top:41px;font-size:5px;letter-spacing:1px}

  /* Medium rectangle 264 x 264 */
  .ad--rectangle{left:825px;top:58px;width:264px;height:264px}
  .ad--rectangle .ad__prevents{right:13px;top:24px;font-size:18px}
  .ad--rectangle .ad__headline{right:11px;top:41px;font-size:42px}
  .ad--rectangle .ad__sub{right:13px;top:80px;font-size:18px}
  .ad--rectangle .ad__photo{left:7px;top:100px;width:150px;height:124px}
  .ad--rectangle .ad__brand{right:16px;top:128px;font-size:11px}
  .ad--rectangle .ad__url{left:23px;top:234px;font-size:6.5px;letter-spacing:1.5px}
  .ad--rectangle .ad__cta{right:15px;top:229px;width:88px;height:16px;font-size:10px}

  /* Square 220 x 220 */
  .ad--square{left:825px;top:374px;width:220px;height:220px}
  .ad--square .ad__prevents{right:12px;top:24px;font-size:12px}
  .ad--square .ad__headline{right:12px;top:36px;font-size:32px}
  .ad--square .ad__sub{right:13px;top:65px;font-size:12px;letter-spacing:.02em}
  .ad--square .ad__photo{left:10px;top:82px;width:130px;height:100px}
  .ad--square .ad__brand{right:14px;top:102px;font-size:9px}
  .ad--square .ad__url{left:13px;top:193px;font-size:5px;letter-spacing:1px}
  .ad--square .ad__cta{right:17px;top:186px;width:76px;height:14px;font-size:8.5px}

  /* Skyscraper 131 x 497 */
  .ad--skyscraper{left:839px;top:649px;width:131px;height:497px}
  .ad--skyscraper .ad__photo{left:5px;top:46px;width:120px;height:114px}
  .ad--skyscraper .ad__prevents{left:0;right:0;text-align:center;top:168px;font-size:16px}
  .ad--skyscraper .ad__headline{left:0;right:0;text-align:center;top:182px;font-size:58px;line-height:52px;white-space:normal}
  .ad--skyscraper .ad__sub{left:0;right:0;text-align:center;top:339px;font-size:13.5px;letter-spacing:0}
  .ad--skyscraper .ad__brand{left:0;right:0;justify-content:center;top:398px;font-size:12px}
  .ad--skyscraper .ad__url{left:0;right:0;text-align:center;top:432px;font-size:6px;letter-spacing:1.5px}
  .ad--skyscraper .ad__cta{left:13px;top:454px;width:100px;height:21px;font-size:12px}
</style>
</head>
<body>

<!-- Facebook -->
<section class="ad ad--facebook">
  <svg class="ad__corner" width="73" height="91"><polygon points="0,0 73,0 0,91"/></svg>
  <div class="ad__photo" role="img" aria-label="Red sedan parked, with a magnified view of red protective pads fitted on its door"></div>
  <div class="ad__brand">brimvaxo</div>
  <div class="ad__prevents">PREVENTS</div>
  <div class="ad__headline">DENTS AND CHIPS</div>
  <div class="ad__sub">WHEN PARKED</div>
  <div class="ad__cta">Learn more <svg viewBox="0 0 20 20"><circle cx="10" cy="10" r="10" fill="#fff"/><polygon points="8,5.5 15,10 8,14.5" fill="#d4171d"/></svg></div>
  <div class="ad__url">www.brimvaxo.com</div>
</section>
<div class="label" style="left:335px;top:454px;font-size:19px">FACEBOOK</div>

<!-- Twitter -->
<section class="ad ad--twitter">
  <svg class="ad__corner" width="82" height="104"><polygon points="0,0 82,0 0,104"/></svg>
  <div class="ad__photo" role="img" aria-label="Red sedan parked, with a magnified view of red protective pads fitted on its door"></div>
  <div class="ad__brand">brimvaxo</div>
  <div class="ad__prevents">PREVENTS</div>
  <div class="ad__headline">DENTS AND CHIPS</div>
  <div class="ad__sub">WHEN PARKED</div>
  <div class="ad__cta">Learn more <svg viewBox="0 0 20 20"><circle cx="10" cy="10" r="10" fill="#fff"/><polygon points="8,5.5 15,10 8,14.5" fill="#d4171d"/></svg></div>
  <div class="ad__url">www.brimvaxo.com</div>
</section>
<div class="label" style="left:335px;top:878px;font-size:19px">TWITTER</div>

<!-- 728 x 90 -->
<section class="ad ad--leaderboard">
  <svg class="ad__corner" width="46" height="36"><polygon points="0,0 46,0 0,36"/></svg>
  <div class="ad__photo" role="img" aria-label="Red sedan with a magnified view of a door pad"></div>
  <div class="ad__prevents">PREVENTS</div>
  <div class="ad__headline">DENTS AND CHIPS</div>
  <div class="ad__sub">WHEN PARKED</div>
  <div class="ad__cta">Learn more <svg viewBox="0 0 20 20"><circle cx="10" cy="10" r="10" fill="#fff"/><polygon points="8,5.5 15,10 8,14.5" fill="#d4171d"/></svg></div>
  <div class="ad__brand">brimvaxo</div>
  <div class="ad__url">www.brimvaxo.com</div>
</section>
<div class="label" style="left:318px;top:1035px;font-size:19px">728 X 90</div>

<!-- 468 x 60 -->
<section class="ad ad--banner">
  <svg class="ad__corner" width="34" height="34"><polygon points="0,0 34,0 0,34"/></svg>
  <div class="ad__photo" role="img" aria-label="Red sedan with a magnified view of a door pad"></div>
  <div class="ad__prevents">PREVENTS</div>
  <div class="ad__headline">DENTS AND CHIPS</div>
  <div class="ad__sub">WHEN PARKED</div>
  <div class="ad__cta">Learn more <svg viewBox="0 0 20 20"><circle cx="10" cy="10" r="10" fill="#fff"/><polygon points="8,5.5 15,10 8,14.5" fill="#d4171d"/></svg></div>
  <div class="ad__brand">brimvaxo</div>
  <div class="ad__url">www.brimvaxo.com</div>
</section>
<div class="label" style="left:286px;top:1139px;font-size:19px">468 X 60</div>

<!-- 300 x 250 -->
<section class="ad ad--rectangle">
  <svg class="ad__corner" width="47" height="64"><polygon points="0,0 47,0 0,64"/></svg>
  <div class="ad__prevents">PREVENTS</div>
  <div class="ad__headline">DENTS AND CHIPS</div>
  <div class="ad__sub">WHEN PARKED</div>
  <div class="ad__photo" role="img" aria-label="Red sedan with a magnified view of red door pads"></div>
  <div class="ad__brand">brimvaxo</div>
  <div class="ad__url">www.brimvaxo.com</div>
  <div class="ad__cta">Learn more <svg viewBox="0 0 20 20"><circle cx="10" cy="10" r="10" fill="#fff"/><polygon points="8,5.5 15,10 8,14.5" fill="#d4171d"/></svg></div>
</section>
<div class="label" style="left:956px;top:333px;font-size:19px">300 X 250</div>

<!-- 250 x 250 -->
<section class="ad ad--square">
  <svg class="ad__corner" width="50" height="68"><polygon points="0,0 50,0 0,68"/></svg>
  <div class="ad__prevents">PREVENTS</div>
  <div class="ad__headline">DENTS AND CHIPS</div>
  <div class="ad__sub">WHEN PARKED</div>
  <div class="ad__photo" role="img" aria-label="Red sedan with a magnified view of red door pads"></div>
  <div class="ad__brand">brimvaxo</div>
  <div class="ad__url">www.brimvaxo.com</div>
  <div class="ad__cta">Learn more <svg viewBox="0 0 20 20"><circle cx="10" cy="10" r="10" fill="#fff"/><polygon points="8,5.5 15,10 8,14.5" fill="#d4171d"/></svg></div>
</section>
<div class="label" style="left:943px;top:602px;font-size:19px">250 X 250</div>

<!-- 160 x 600 -->
<section class="ad ad--skyscraper">
  <svg class="ad__corner" width="57" height="71"><polygon points="0,0 57,0 0,71"/></svg>
  <div class="ad__photo" role="img" aria-label="Red sedan with a magnified view of red door pads"></div>
  <div class="ad__prevents">PREVENTS</div>
  <div class="ad__headline">DENTS<br>AND<br>CHIPS</div>
  <div class="ad__sub">WHEN PARKED</div>
  <div class="ad__brand">brimvaxo</div>
  <div class="ad__url">www.brimvaxo.com</div>
  <div class="ad__cta">Learn more <svg viewBox="0 0 20 20"><circle cx="10" cy="10" r="10" fill="#fff"/><polygon points="8,5.5 15,10 8,14.5" fill="#d4171d"/></svg></div>
</section>
<div class="label" style="left:905px;top:1162px;font-size:19px">160 X 600</div>

</body>
</html>
```